Spiritual journeyer, astrologer, Reiki master, underground music lover needs business card design

Initially I need a business card design (and possibly a logo for my new website). I offer astrological and energetic inquiry and guidance to clients in support of their life's evolutionary path. I combine an eclectic mix of methods with a focus on the mind body connection. I am a spiritual journeyer, astrologer, Reiki Master, certified personal trainer, soon to be black belt in Taekwondo (karate), and researcher into the benefits of music/sound vibrational therapy. And underground music lover :) The attached drawing is just something I drew freehand, it is symbolic of many things important to me. I wanted the figure to clearly be female. Her arms are open to catch the sky, the name of my new business is Orlabrook, and Orla is my daughter's name. This was just an idea I had, I'm open to suggestions. The photo is me with the planets in the sky as they were at the moment I was born (some years ago-LOL)
Updates

I have picked a final design. Thank you everyone for your time and effort.

Target Market(s)

Worldwide, what I do can be done in person or anywhere in the world via Skype

Industry/Entity Type

Professional Service

Contact Information for Business Card

Simple, unusual image with my business name and contact info

Font styles to use
Sans Serif

Requirements
Must have
• My website very clean, simple. Somehow combine biz name of Orlabrook with female figure catching/holding the starry sky? See my poor drawing I attached.
Nice to have
• Something that conveys all the unique, unusual, eclectic skills and capacities I have
Should not have
• Frilly, fancy, stuffy

```html
<!DOCTYPE html>
<html lang="en">
<head>
<meta charset="utf-8">
<title>Orlabrook business card</title>
<link rel="stylesheet" href="https://fonts.googleapis.com/css2?family=Open+Sans:wght@400;600&display=swap">
<style>
  :root {
    --page: #4a4a4a;
    --night-deep: #0b0c22;
    --night-mid: #17183a;
    --sky-light: #bfe6fb;
    --sky-mid: #4d8fe0;
    --sky-deep: #1d3fae;
    --edge-blue: #3350d8;
    --logo-ink: #1b2438;
    --accent: #f4a62a;
    --text-light: #f4f6fb;
    --divider: #3fa6d8;
  }
  * { margin: 0; padding: 0; box-sizing: border-box; }
  html, body { width: 1200px; height: 1023px; overflow: hidden; }
  body {
    background: var(--page);
    font-family: "Open Sans", sans-serif;
    position: relative;
  }
  .card {
    position: absolute;
    left: 180px; top: 271px;
    width: 840px; height: 480px;
    border-radius: 14px;
    overflow: hidden;
    background: linear-gradient(160deg, var(--night-mid), var(--night-deep));
  }
  .card-art { position: absolute; inset: 0; }
  .brand {
    position: absolute;
    left: 0; right: 0; top: 112px;
    display: flex; align-items: center; justify-content: center; gap: 14px;
    color: var(--logo-ink);
    font-size: 54px; font-weight: 400; letter-spacing: 1px;
  }
  .brand-dot {
    width: 20px; height: 20px; border-radius: 50%;
    background: var(--logo-ink);
  }
  .identity { position: absolute; left: 70px; top: 300px; }
  .name {
    color: var(--accent);
    font-size: 34px; font-weight: 600; letter-spacing: 0.5px;
    line-height: 1.1;
  }
  .role {
    color: var(--text-light);
    font-size: 19px; font-weight: 600; line-height: 1.45;
    margin-top: 10px; padding-left: 70px;
  }
  .divider {
    position: absolute; left: 500px; top: 300px;
    width: 1px; height: 120px;
    background: linear-gradient(var(--divider), transparent);
  }
  .contacts {
    position: absolute; left: 525px; top: 298px;
    list-style: none;
    color: var(--text-light);
    font-size: 19px; font-weight: 600;
  }
  .contacts li {
    display: flex; align-items: center; gap: 12px;
    height: 38px;
  }
  .contact-icon { width: 20px; height: 20px; flex: none; }
</style>
</head>
<body>
  <div class="card">
    <svg class="card-art" viewBox="0 0 840 480" width="840" height="480">
      <defs>
        <radialGradient id="skyGlow" cx="0.55" cy="0.55" r="0.7">
          <stop offset="0" stop-color="var(--sky-light)"/>
          <stop offset="0.45" stop-color="var(--sky-mid)"/>
          <stop offset="1" stop-color="var(--sky-deep)"/>
        </radialGradient>
        <linearGradient id="figureHaze" x1="0" y1="0" x2="1" y2="1">
          <stop offset="0" stop-color="#1e2048" stop-opacity="0.6"/>
          <stop offset="1" stop-color="#0b0c22" stop-opacity="0"/>
        </linearGradient>
      </defs>
      <rect class="zodiac-figures" role="img" aria-label="Faint zodiac constellation figures over a starry night sky" x="0" y="230" width="840" height="250" fill="url(#figureHaze)"/>
      <path class="sky-band" role="img" aria-label="Glowing starry sky" d="M0 0 H840 V190 Q420 300 0 190 Z" fill="url(#skyGlow)"/>
      <path d="M0 192 Q420 302 840 192" fill="none" stroke="var(--logo-ink)" stroke-width="5"/>
      <path d="M0 202 Q420 312 840 202" fill="none" stroke="var(--edge-blue)" stroke-width="6"/>
    </svg>

    <div class="brand"><span class="brand-dot"></span>Orlabrook</div>

    <div class="identity">
      <p class="name">MAREN ELLISON</p>
      <p class="role">Astrological and Energetic<br>Guidance and Inquiry</p>
    </div>

    <div class="divider"></div>

    <ul class="contacts">
      <li>
        <svg class="contact-icon" viewBox="0 0 20 20"><circle cx="10" cy="10" r="10" fill="var(--accent)"/><path d="M6.5 5.5l2 0 1 2.5-1.2 1a6 6 0 0 0 2.7 2.7l1-1.2 2.5 1v2a1 1 0 0 1-1 1A8 8 0 0 1 5.5 6.5a1 1 0 0 1 1-1z" fill="var(--night-deep)"/></svg>
        555-014-2290
      </li>
      <li>
        <svg class="contact-icon" viewBox="0 0 20 20"><circle cx="10" cy="10" r="10" fill="var(--accent)"/><rect x="5" y="6.5" width="10" height="7" rx="1" fill="var(--night-deep)"/><path d="M5.5 7l4.5 3.5L14.5 7" fill="none" stroke="var(--accent)" stroke-width="1"/></svg>
        email@orlabrook.com
      </li>
      <li>
        <svg class="contact-icon" viewBox="0 0 20 20"><circle cx="10" cy="10" r="10" fill="var(--accent)"/><g fill="none" stroke="var(--night-deep)" stroke-width="1.2"><circle cx="10" cy="10" r="5.5"/><ellipse cx="10" cy="10" rx="2.4" ry="5.5"/><path d="M4.5 10h11"/></g></svg>
        www.orlabrook.com
      </li>
    </ul>
  </div>
</body>
</html>
```